Astrophotography equipment infographic

Hi! We need an infographic that displays different equipment used for astrophotography. Please see attached for further details.

```html
<!DOCTYPE html>
<html lang="en">
<head>
<meta charset="utf-8">
<title>Astrophotography Equipment</title>
<link rel="stylesheet" href="https://fonts.googleapis.com/css2?family=Oswald:wght@500;600&family=Barlow:wght@400;500;600;700&family=Barlow+Semi+Condensed:wght@400;500;600&display=swap">
<style>
  :root {
    --stage: #000000;
    --paper: #ffffff;
    --ink: #1e1c48;
    --night-deep: #2c2868;
    --night-mid: #5a3f88;
    --night-pink: #a7599f;
    --planet: #8f86c4;
    --haze-dark: #8ea4b3;
    --haze-light: #c8dde8;
  }
  * { margin: 0; padding: 0; box-sizing: border-box; }
  html, body {
    width: 1200px; height: 1000px; overflow: hidden;
    background: var(--stage);
  }
  .poster {
    position: absolute; left: 295px; top: 112px;
    width: 610px; height: 774px;
    background: var(--paper);
    overflow: hidden;
    color: var(--ink);
    font-family: "Barlow Semi Condensed", "Barlow", sans-serif;
  }
  .sky-band { position: absolute; left: 0; top: 0; width: 610px; height: 200px; }
  .poster-title {
    position: absolute; left: 0; right: 0; top: 30px;
    text-align: center;
    font-family: "Oswald", sans-serif; font-weight: 500;
    font-size: 38px; letter-spacing: 0.5px;
    color: var(--paper);
  }
  .art { position: absolute; }
  .art-ringed-planet {
    left: 388px; top: 108px; width: 116px; height: 78px;
    border-radius: 50%;
    background: radial-gradient(circle at 50% 50%, #9a93cf 0 34%, #7b6fb8 35% 44%, rgba(123,111,184,0.35) 45% 70%, transparent 71%);
  }
  .art-small-planet {
    left: 552px; top: 13px; width: 36px; height: 36px; border-radius: 50%;
    background: linear-gradient(135deg, #d9d4ec, #8e87b8);
  }
  .art-gear {
    left: 395px; top: 402px; width: 215px; height: 162px;
    border-radius: 90px 0 0 90px / 70px 0 0 70px;
    background: linear-gradient(135deg, #7d4c9c 0%, #a7599f 100%);
  }
  .art-ground {
    left: 0; top: 585px; width: 355px; height: 189px;
    border-radius: 0 160px 0 0 / 0 150px 0 0;
    background: linear-gradient(180deg, var(--haze-dark) 0%, var(--haze-light) 100%);
  }
  .intro {
    position: absolute; left: 28px; top: 168px;
    font-family: "Barlow", sans-serif; font-weight: 600;
    font-size: 17px; line-height: 22px;
  }
  .setup { position: absolute; }
  .setup-right { right: 28px; text-align: right; }
  .setup-left { left: 28px; text-align: left; }
  .setup-title {
    font-family: "Barlow", sans-serif; font-weight: 600;
    font-size: 18.5px; line-height: 22px;
  }
  .setup-example {
    font-family: "Barlow", sans-serif; font-weight: 600;
    font-size: 13.5px; line-height: 18px;
    margin-bottom: 6px;
  }
  .setup-list { list-style: none; font-size: 12.5px; line-height: 17.3px; }
  .site-url {
    position: absolute; right: 28px; top: 726px;
    font-family: "Barlow", sans-serif; font-weight: 500; font-size: 17px;
  }
</style>
</head>
<body>
<main class="poster">
  <svg class="sky-band" viewBox="0 0 610 200" aria-hidden="true">
    <defs>
      <linearGradient id="nightSky" x1="0" y1="0" x2="1" y2="0.3">
        <stop offset="0" stop-color="#2c2868"/>
        <stop offset="0.5" stop-color="#5a3f88"/>
        <stop offset="1" stop-color="#a7599f"/>
      </linearGradient>
    </defs>
    <path d="M0 0 H610 V120 C585 150 545 140 520 135 C480 128 460 150 420 150 C385 150 375 110 330 110 C280 110 260 125 215 118 C175 112 150 95 110 110 C75 123 45 135 0 128 Z" fill="url(#nightSky)"/>
  </svg>

  <h1 class="poster-title">ASTROPHOTOGRAPHY EQUIPMENT</h1>

  <div class="art art-small-planet" role="img" aria-label="Illustration of a small striped planet"></div>
  <div class="art art-ringed-planet" role="img" aria-label="Illustration of a ringed planet"></div>

  <p class="intro">Typical equipment set-ups<br>for different kinds of astrophotography:</p>

  <section class="setup setup-right" style="top:246px;">
    <h2 class="setup-title">1. For landscape astrophotography</h2>
    <p class="setup-example">(for example, capturing the Milky Way above a landscape)</p>
    <ul class="setup-list">
      <li>1) Regular DSLR camera (or mirrorless interchangeable lens camera)</li>
      <li>A camera with a full-frame sensor is best, but not required</li>
      <li>2) Wide angle lens (35mm or below for a full-frame camera, 24mm or below for an APS-C sensor camera)</li>
      <li>3) Tripod (the sturdier the better)</li>
      <li>4) Star tracker (optional). These sit between a camera and tripod and move the camera</li>
      <li>with the rotation of the earth, allowing longer exposures without star trails appearing.</li>
    </ul>
  </section>

  <div class="art art-gear" role="img" aria-label="Illustration of a camera and a telescope on a purple backdrop"></div>

  <section class="setup setup-left" style="top:428px;">
    <h2 class="setup-title">2. For Solar System astrophotography</h2>
    <p class="setup-example">(for example, sun, moon, saturn, jupiter and other planets)</p>
    <ul class="setup-list">
      <li>1) Regular DSLR camera (or mirrorless interchangeable lens camera)</li>
      <li>2) Telephoto lens (85mm to 300mm upwards)</li>
      <li>3) Tripod (the sturdier the better)</li>
      <li>4) Star tracker (optional)</li>
    </ul>
  </section>

  <div class="art art-ground" role="img" aria-label="Illustration of a telescope on a tripod against pale blue hills"></div>

  <section class="setup setup-right" style="top:584px;">
    <h2 class="setup-title">3. For deep sky astrophotography</h2>
    <p class="setup-example">(galaxies, nebulae etc)</p>
    <ul class="setup-list">
      <li>1) Specialist astrophotography camera (eg, CCD camera)</li>
      <li>or adapted DSLR camera with IR filter.</li>
      <li>2) Telescope - with the camera attached this works in</li>
      <li>place of a camera lens.</li>
      <li>3) Tripod (and telescope mount)</li>
    </ul>
  </section>

  <p class="site-url">nightlensguides.com</p>
</main>
</body>
</html>
```